Booth Panels- VerdelleWorks Beauty Product Manufacturer

Hi,

We are purchasing a ready-made booth for private label tradeshows. We need more design elements to make the booth look beautiful. Use you're imagination! I've attached elements we have used in the past. But we need more and better.

Please ignore the visuals of image004 and image003 (tattoo element)- That is just showing the layout of the booth. Center panel (w/ tv) / Right panel 10'

The actual die lines are attached.

Company website: verdelleworks.com < note the company website is barebones so don't follow that theme. We need the booth to capture the eye.

Thank you,
Theo

```html
<!DOCTYPE html>
<html lang="en">
<head>
<meta charset="utf-8">
<title>VerdelleWorks Booth Panels</title>
<link href="https://fonts.googleapis.com/css2?family=Montserrat:wght@400;500;600;800&display=swap" rel="stylesheet">
<style>
  :root {
    --backdrop: #c9c9c9;
    --panel: #e2dbc9;
    --brand-green: #0c8443;
    --ink: #262626;
    --ring-brown: #7a634f;
    --photo-peach: #e3b08c;
    --photo-linen: #d9cdb8;
    --photo-loofah: #8a7560;
    --photo-jade: #7f9a55;
    --strip-light: #efe8e0;
    --strip-pink: #eccfca;
    --strip-cream: #f4eadc;
  }
  * { margin: 0; padding: 0; box-sizing: border-box; }
  html, body { width: 1200px; height: 1200px; overflow: hidden; background: var(--backdrop); }
  body { font-family: "Montserrat", sans-serif; color: var(--ink); }
  .booth { position: relative; width: 1200px; height: 1200px; }
  .booth-shapes { position: absolute; inset: 0; }

  .brand-name {
    position: absolute; left: 138px; top: 403px;
    font-size: 22px; font-weight: 500; color: var(--brand-green); letter-spacing: 0.3px;
    display: flex; align-items: center; gap: 8px;
  }
  .brand-name .dot { width: 11px; height: 11px; border-radius: 50%; background: var(--brand-green); }

  .section-title {
    position: absolute; font-weight: 800; color: var(--brand-green);
    font-size: 23px; line-height: 25px; letter-spacing: 0.6px;
  }
  .why-title { left: 142px; top: 485px; }
  .who-title { left: 799px; top: 300px; }

  .point-list { position: absolute; list-style: none; }
  .point {
    position: absolute; left: 0; white-space: nowrap;
    font-size: 17.5px; line-height: 24px; letter-spacing: 0.5px; font-weight: 400;
    padding-left: 30px;
  }
  .point::before {
    content: ""; position: absolute; left: 2px; top: 2px;
    width: 12px; height: 20px; border: 1px solid var(--brand-green);
    border-radius: 50% 50% 50% 50% / 60% 60% 40% 40%; opacity: 0.75;
  }
  .point::after {
    content: ""; position: absolute; left: 8px; top: 5px;
    width: 1px; height: 14px; background: var(--brand-green); opacity: 0.6;
  }
  .why-list { left: 146px; top: 0; }
  .who-list { left: 800px; top: 0; }

  .phone {
    position: absolute; left: 815px; top: 734px;
    font-size: 27px; font-weight: 600; color: var(--brand-green); letter-spacing: 1.2px;
  }
  .web {
    position: absolute; left: 817px; top: 774px;
    font-size: 16px; font-weight: 500; color: var(--ink);
  }
</style>
</head>
<body>
<main class="booth">
  <svg class="booth-shapes" width="1200" height="1200" viewBox="0 0 1200 1200">
    <defs>
      <clipPath id="left-panel-clip">
        <path d="M101 1012 V226 Q101 184 142 188 L722 274 Q759 280 759 318 V1012 Z"/>
      </clipPath>
      <clipPath id="right-panel-clip">
        <path d="M761 1012 V292 Q761 262 792 254 L1060 190 Q1098 182 1098 222 V1012 Z"/>
      </clipPath>
      <linearGradient id="strip-tones" x1="0" x2="1" y1="0" y2="0">
        <stop offset="0" stop-color="var(--strip-cream)"/>
        <stop offset="0.2" stop-color="var(--strip-pink)"/>
        <stop offset="0.45" stop-color="var(--strip-light)"/>
        <stop offset="0.7" stop-color="var(--strip-pink)"/>
        <stop offset="1" stop-color="var(--strip-cream)"/>
      </linearGradient>
      <linearGradient id="strip-fade" x1="0" x2="0" y1="0" y2="1">
        <stop offset="0" stop-color="var(--panel)" stop-opacity="1"/>
        <stop offset="0.35" stop-color="var(--panel)" stop-opacity="0"/>
      </linearGradient>
      <radialGradient id="photo-tones" cx="0.55" cy="0.45" r="0.55">
        <stop offset="0" stop-color="var(--photo-loofah)"/>
        <stop offset="0.35" stop-color="var(--photo-jade)" stop-opacity="0.9"/>
        <stop offset="0.6" stop-color="var(--photo-linen)"/>
        <stop offset="1" stop-color="var(--photo-peach)"/>
      </radialGradient>
    </defs>

    <g class="left-panel" clip-path="url(#left-panel-clip)">
      <rect x="100" y="180" width="670" height="840" fill="var(--panel)"/>
      <path class="green-sweep" d="M255 203 L770 272 L770 612 L725 585 L690 545 L640 500 L600 470 L560 440 L540 420 L505 385 L470 345 L430 300 L380 262 L330 230 Z" fill="var(--brand-green)"/>
      <g role="img" aria-label="Photo of skincare bottles, jars, a jade stone and a loofah in a linen bowl, framed by a brown brush ring">
        <circle cx="612" cy="640" r="180" fill="none" stroke="var(--ring-brown)" stroke-width="24"/>
        <circle cx="618" cy="642" r="154" fill="url(#photo-tones)"/>
      </g>
      <rect role="img" aria-label="Photo of cream jars, pink pump bottles and small pale roses on a light surface" x="100" y="840" width="670" height="175" fill="url(#strip-tones)"/>
      <rect x="100" y="840" width="670" height="175" fill="url(#strip-fade)"/>
    </g>

    <g class="right-panel" clip-path="url(#right-panel-clip)">
      <rect x="760" y="180" width="345" height="840" fill="var(--panel)"/>
      <rect role="img" aria-label="Photo of cream jars, pink pump bottles and small pale roses on a light surface" x="760" y="840" width="345" height="175" fill="url(#strip-tones)"/>
      <rect x="760" y="840" width="345" height="175" fill="url(#strip-fade)"/>
    </g>
  </svg>

  <div class="brand-name"><span class="dot"></span>VerdelleWorks</div>

  <h2 class="section-title why-title">WHY LOOK<br>ANY FURTHER?</h2>
  <ul class="point-list why-list">
    <li class="point" style="top:551px">HIGHEST QUALITY</li>
    <li class="point" style="top:594px">UNBEATABLE PRICING</li>
    <li class="point" style="top:637px">FAST TURNAROUND</li>
    <li class="point" style="top:680px">UNRIVALED CUSTOMER<br>SERVICE</li>
    <li class="point" style="top:749px">LOW MINIMUMS</li>
    <li class="point" style="top:792px">CUSTOM FORMULATIONS</li>
  </ul>

  <h2 class="section-title who-title">WHO WE ARE</h2>
  <ul class="point-list who-list">
    <li class="point" style="top:348px">FAMILY-OWNED<br>SINCE 1994</li>
    <li class="point" style="top:417px">BASED IN<br>LOS ANGELES, CA</li>
    <li class="point" style="top:486px">50,000 sq. ft. FACILITY</li>
    <li class="point" style="top:530px">FORMULATING,<br>COMPOUNDING,<br>FILLING, AND<br>PACKAGING</li>
    <li class="point" style="top:646px">FULLY LICENSED AND<br>cGMP COMPLIANT</li>
  </ul>

  <p class="phone">(555)214-7380</p>
  <p class="web">www.verdelleworks.com</p>
</main>
</body>
</html>
```